RepHarborly.com "RE-SKIN" project

We have an existing site that we've recently built that needs to be re-formatted, skinned and polished. Our current developer did an amazing job building the backend but it not an expert in design and formatting of HTML and Web design. We need to have site cleaned up with all new formatting, layout, design elements and visual effects. ALl the date and functionality of the site will remain the same.

We would like to see Home page mock ups that may include Photo's, Flash, etc. or any other design element the designer feels would convey, a corporate, business oriented, simple and clean feel. The way the site currently looks is very basic and we need to have a slick, visual pleasing and easy to navigate design to go with our new functionality. The home page design will then need to translate over into the remaining pages of the site.

This is business to business site and will act as recruitment tool for medical device organizations. We have created a nationwide database of the top medical distributor groups (independent sale reps and groups). We act a "dating site" for medical manufacturers to find the best reps to sell their products.

NOTES on DESIGN:

* THE FUNCTION AND DATA OF THE SITE WILL REMAIN THE SAME, THIS PROJECT WILL BE TAKING ALL EXISTING INFO AND RE-DESIGNING THE LAYOUT.

*Must keep same color scheme

*Home Page design will be main focus and then ALL other pages need to follow style and template of Home page

* The sign up process on the site is in desperate need of re-design and we would like to see BIG, Step by Step, windows that make it feel very simple for the user to fill out (Best example we can think of is the Wellpathory.org site step by step sign up process. As bad as the overall functionality is on that site, the sign up process and drop down menu steps are easy to fill out.)

*The site is currently in a very basic "utilitarian" style and has very little in way of design, text formatting, and overall appearance. We need to have the designer go through each page and JUSTIFY, RE-SIZE, RE-SCALE and dress up all the current information displayed.

* We need the display pages to be easier to read, have better flow and more visually pleasing. (EXAMPLE: ANy search results that are done on the site come back in very table driven, hard to read, small text with small logo. We would like to see more design elements with updated formats and hopefully larger icons and east to read and navigate text

* WE ARE OPEN TO ANY DESIGN IDEAS OR MOCK UPS.

* Logos, icons, animation etc need to remain the same.

*Home page can feature video or photos but the remainder of the site will remian data only.
Updates

We would suggest doing a Mock up of the HOME PAGE only to begin with. We can then evaluate and choose a design theme/concept to carry over into the remainder of the pages.

Target Market(s)

Independent Medical Sales Distributors (sales reps) and Medical device manufacturers.

Industry/Entity Type

Recruitment

Coding

Coded - Design and coding required

Number of Pages Required

5+ page

Font styles to use
Sans Serif

Colors
0492cd
0455a3
3176b5
cedeed
85cae6
fcfdfe

Requirements
Must have
• *Must be Mobile Friendly
• *Must use all the info, links, logos and icons currently on www.RepHarborly.com
• *All pages of the site must follow to layout and design of the Home Page that is created in this project
• *Every page needs to be updated
Nice to have
• Glossy, crisp home page, that incorporate "stock" photos or animation for a more promotional or brochure type of feel
• Easy to navigate, bigger text and buttons and icons.
Should not have
• Color scheme and logo should not change

```html
<!DOCTYPE html>
<html lang="en">
<head>
<meta charset="utf-8">
<title>RepHarborly.com – Home</title>
<link href="https://fonts.googleapis.com/css2?family=IBM+Plex+Sans:wght@300;400;500;600;700&display=swap" rel="stylesheet">
<style>
:root{
  --blue:#0492cd;
  --blue-dark:#0455a3;
  --blue-mid:#3176b5;
  --blue-pale:#cedeed;
  --blue-light:#85cae6;
  --white:#fcfdfe;
  --navy:#262a39;
  --footer:#252633;
  --ink:#2b2f3a;
  --grey:#6b7180;
  --line:#d6dbe2;
  --panel:#f1f3f6;
}
*{box-sizing:border-box;margin:0;padding:0}
html,body{width:1200px;height:3255px;overflow:hidden}
body{position:relative;background:#fff;font-family:"IBM Plex Sans",sans-serif;color:var(--ink)}
.abs{position:absolute}

/* header */
.site-header{position:absolute;left:0;top:0;width:1200px;height:98px;background:var(--white);z-index:3}
.brand{position:absolute;left:156px;top:20px;display:flex;align-items:center;gap:8px;font-size:28px;font-weight:600;color:var(--blue-dark);letter-spacing:-.5px}
.brand-mark{width:30px;height:30px;background:var(--blue);border-radius:6px}
.call{position:absolute;left:497px;top:26px;font-size:17px;color:var(--blue);font-weight:500;display:flex;align-items:center;gap:6px}
.call b{color:var(--blue-dark);font-weight:600}
.signin{position:absolute;left:738px;top:24px;width:174px;height:32px;border-radius:16px;background:var(--blue-dark);color:#fff;font-size:11px;font-weight:600;display:flex;align-items:center;justify-content:center;gap:6px;letter-spacing:.4px}
.social{position:absolute;display:flex;gap:8px}
.social span{display:block;width:26px;height:26px;border-radius:50%;background:#8a8f99}
.social span.on{background:var(--blue)}
.site-header .social{left:946px;top:27px}

/* nav */
.main-nav{position:absolute;left:156px;top:78px;width:888px;height:41px;background:var(--blue);display:flex;z-index:4}
.main-nav a{color:#fff;text-decoration:none;font-size:12.5px;font-weight:500;padding:0 22px;display:flex;align-items:center}
.main-nav a.active{background:var(--blue-dark)}
.main-nav a .car{font-size:9px;margin-left:5px}

/* hero */
.hero{position:absolute;left:0;top:98px;width:1200px;height:440px;background:radial-gradient(ellipse at 65% 55%,#5c6066 0%,#3b3e44 45%,#25272b 100%)}
.hero h1{position:absolute;left:0;width:1200px;top:118px;text-align:center;color:#fff;font-weight:400;font-size:28px;line-height:40px}
.hero h1 strong{font-weight:500}
.search{position:absolute;top:225px;left:232px;display:flex;gap:17px}
.select{width:176px;height:31px;border-radius:16px;background:#c9ccd1;color:#5a5f69;font-size:10px;display:flex;align-items:center;justify-content:space-between;padding:0 14px}
.select.s2{width:185px}
.search .go{width:135px;height:31px;border-radius:16px;background:var(--blue);color:#fff;font-size:11px;font-weight:600;display:flex;align-items:center;justify-content:center;letter-spacing:.3px}
.hero .tag{position:absolute;top:290px;width:1200px;text-align:center;color:#fff;font-size:22px;font-weight:300}
.hero .tag strong{font-weight:600}
.chev{position:absolute;left:592px;top:392px}

/* about */
.about{position:absolute;left:0;top:538px;width:1200px;height:504px;background:linear-gradient(180deg,#ffffff 0%,#eef0f3 45%,#e2e5ea 100%)}
.eyebrow{position:absolute;left:156px;top:80px;font-size:10px;font-weight:600;letter-spacing:1.6px;color:var(--blue-dark)}
.about h2{position:absolute;left:156px;top:106px;font-size:32px;font-weight:400;line-height:42px;color:var(--ink)}
.rule{position:absolute;height:1px;background:#b9bec7}
.about .copy{position:absolute;left:612px;top:108px;width:432px;font-size:12.5px;line-height:19.5px;color:var(--grey)}
.about .copy p+p{margin-top:14px}
.about .copy .hl{color:var(--blue);font-weight:600}
.btn-pill{position:absolute;height:31px;border-radius:16px;font-size:11px;font-weight:600;display:flex;align-items:center;justify-content:center;letter-spacing:.4px}
.about .btn-pill{left:612px;top:317px;width:128px;background:var(--blue-dark);color:#fff}

/* audience cards */
.card-dark{position:absolute;left:536px;top:966px;width:508px;height:564px;background:var(--navy);color:#fff}
.card-blue{position:absolute;left:156px;top:1358px;width:506px;height:476px;background:var(--blue);color:#fff}
.card-dark h3,.card-blue h3{position:absolute;left:76px;font-size:32px;font-weight:400;line-height:42px}
.card-dark h3{top:68px}
.card-blue h3{top:65px}
.card-dark p,.card-blue p{position:absolute;left:76px;font-size:17px;line-height:25px;font-weight:300}
.card-dark p{top:200px}
.card-blue p{top:198px}
.btn-ghost{border:1px solid #fff;color:#fff;width:126px}
.btn-white{background:#fff;color:var(--blue);width:128px}
.photo{position:absolute}

/* products */
.section-title{position:absolute;font-size:32px;font-weight:400;color:var(--ink)}
.tabs{position:absolute;left:686px;top:1914px;width:358px;display:flex;font-size:13px;color:var(--grey)}
.tabs span{flex:1;text-align:center;padding-bottom:7px;border-bottom:1px solid var(--line)}
.tabs span.on{color:var(--blue);border-bottom:2px solid var(--blue)}
.plans-bg{position:absolute;left:156px;top:2029px;width:888px;height:310px;background:var(--panel)}
.plan{position:absolute;width:296px;text-align:center}
.plan.featured{background:#fff;box-shadow:0 6px 24px rgba(30,40,60,.14)}
.plan .price{font-size:29px;font-weight:600;color:var(--blue);margin-top:38px}
.plan .pline{width:62px;height:1px;background:#c8ccd3;margin:14px auto 14px}
.plan h4{font-size:15px;font-weight:500;line-height:21px;color:var(--ink)}
.plan .desc{font-size:11px;line-height:17px;color:var(--grey);margin:18px auto 0;width:210px}
.plan .btns{display:flex;justify-content:center;gap:8px;margin-top:26px}
.plan .btns span{width:112px;height:31px;border-radius:16px;border:1px solid var(--blue-dark);color:var(--blue-dark);font-size:10.5px;font-weight:600;display:flex;align-items:center;justify-content:center}
.plan .btns span.fill{background:var(--blue-dark);color:#fff}

/* featured lines */
.lines{position:absolute;left:156px;top:2522px;width:888px;border-collapse:collapse;font-size:10.5px;color:var(--grey);box-shadow:0 2px 8px rgba(30,40,60,.08)}
.lines th{background:var(--blue);color:#fff;font-weight:500;font-size:12.5px;text-align:left;height:29px;padding:0 12px;border-right:1px solid rgba(255,255,255,.45)}
.lines td{vertical-align:top;padding:15px 12px 0;height:97px;line-height:15px;border-right:1px solid var(--line)}
.lines tr.alt td{background:#eef1f5}
.lines tr:first-child td{background:#fff}

/* footer */
.site-footer{position:absolute;left:0;top:2828px;width:1200px;height:427px;background:var(--footer);text-align:center;color:#7a7f8c}
.site-footer .fbrand{position:absolute;left:0;width:1200px;top:86px;display:flex;justify-content:center;align-items:center;gap:10px;font-size:31px;font-weight:600;color:#e9ebef}
.site-footer .fbrand i{display:block;width:38px;height:38px;background:#e9ebef;border-radius:6px}
.site-footer .addr{position:absolute;width:1200px;top:156px;font-size:11px}
.site-footer .fcall{position:absolute;width:1200px;top:176px;font-size:17px;color:var(--blue-mid)}
.site-footer .social{left:540px;top:248px;gap:12px}
.site-footer .social span{width:32px;height:32px;background:#555a66}
.site-footer .social span.on{background:var(--blue)}
.site-footer .copy{position:absolute;width:1200px;top:314px;font-size:11px;line-height:19px}
</style>
</head>
<body>

<header class="site-header">
  <div class="brand"><span class="brand-mark"></span>RepHarborly</div>
  <div class="call">Call Us:
    <svg width="18" height="18" viewBox="0 0 24 24"><circle cx="12" cy="12" r="11" fill="none" stroke="#0455a3" stroke-width="2"/><path d="M8.5 7c.6-.6 1.3-.5 1.7.1l1 1.6c.3.5.2 1.1-.2 1.5l-.6.6c.5 1.2 1.5 2.2 2.7 2.7l.6-.6c.4-.4 1-.5 1.5-.2l1.6 1c.6.4.7 1.1.1 1.7-1.2 1.3-3.4 1-5.6-1.2S7.2 8.2 8.5 7z" fill="#0455a3"/></svg>
    <b>555.214.0387</b></div>
  <div class="signin">
    <svg width="10" height="10" viewBox="0 0 10 10"><circle cx="5" cy="3" r="2.2" fill="#fff"/><path d="M1 10c0-2.5 1.8-4 4-4s4 1.5 4 4z" fill="#fff"/></svg>
    SIGN IN / SIGN UP</div>
  <div class="social"><span></span><span class="on"></span><span></span></div>
</header>

<nav class="main-nav">
  <a class="active">Home</a>
  <a>About Us</a>
  <a>How It Works<span class="car">▾</span></a>
  <a>Products<span class="car">▾</span></a>
  <a>Sign Up<span class="car">▾</span></a>
  <a>Search<span class="car">▾</span></a>
  <a>Resources</a>
  <a>Contact Us</a>
</nav>

<section class="hero" role="img" aria-label="Dark photo of a stethoscope resting on a desk">
  <h1>The Web's Fastest Growing Resource For<br><strong>Independent Medical Sales</strong></h1>
  <div class="search">
    <div class="select">Distributors <span>▾</span></div>
    <div class="select">Select States <span>▾</span></div>
    <div class="select s2">Select Categories <span>▾</span></div>
    <div class="go">SAMPLE SEARCH</div>
  </div>
  <p class="tag">We Match <strong>Distributors</strong> With <strong>Top Prospect Lines!</strong></p>
  <svg class="chev" width="16" height="10" viewBox="0 0 16 10"><path d="M2 2l6 6 6-6" fill="none" stroke="#fff" stroke-width="2"/></svg>
</section>

<section class="about" role="img" aria-label="Soft, pale photo of a medical office in the background">
  <div class="eyebrow">WHO WE ARE</div>
  <h2>We Match Distributors<br>With Top Prospect Lines!</h2>
  <div class="rule" style="left:78px;top:215px;width:280px"></div>
  <div class="copy">
    <p>The independent medical sales arena has exploded over the last decade and an increasing amount of manufacturers are relying on an independent sales model to grow their world wide presence.</p>
    <p><span class="hl">RepHarborly.com</span> is quickly becoming the ideal place for independent sales reps, manufacturers and distributors to connect and build the perfect product portfolio and independent sales team. <span class="hl">simply put, we are the fastest growing resource for independent medical sales opportunities on the web!</span></p>
  </div>
  <div class="btn-pill">DISCOVER MORE</div>
</section>

<div class="card-dark">
  <h3>I Need<br>Distributors</h3>
  <div class="rule" style="left:0;top:170px;width:290px;background:#4a4f5e"></div>
  <p>Find top medical distributor<br>reps or groups to sell your product.</p>
  <div class="btn-pill btn-ghost" style="left:76px;top:274px">SIGN UP NOW!</div>
</div>

<div class="photo" style="left:156px;top:1141px;width:380px;height:217px;background:linear-gradient(135deg,#3d5663 0%,#22313b 55%,#5f7a86 100%)" role="img" aria-label="Photo of hands typing on a keyboard"></div>

<div class="card-blue">
  <h3>I Need<br>New Product Lines</h3>
  <p>Locate and secure the top available<br>medical product lines in your area.</p>
  <div class="btn-pill btn-white" style="left:76px;top:284px">SIGN UP NOW!</div>
</div>
<div class="rule" style="left:78px;top:1532px;width:210px;background:rgba(255,255,255,.55);z-index:2"></div>

<div class="photo" style="left:662px;top:1532px;width:306px;height:221px;background:linear-gradient(135deg,#4b4e55 0%,#30333a 50%,#5a5f68 100%)" role="img" aria-label="Photo of medical supplies laid out on a dark surface"></div>

<h2 class="section-title" style="left:230px;top:1906px">Our Products</h2>
<div class="rule" style="left:78px;top:1973px;width:280px"></div>
<div class="tabs"><span>Distributor Plans</span><span class="on">Manufacturer Plans</span></div>

<div class="plans-bg"></div>
<div class="plan" style="left:156px;top:2029px;height:310px">
  <div class="price">$995.00</div><div class="pline"></div>
  <h4>30 Day Post &amp;<br>Distributor Search Package</h4>
  <p class="desc">Unlimited Job Postings and access to our directory of Distributor Principals and Independent ...</p>
  <div class="btns"><span>MORE DETAIL</span><span>BUY NOW!</span></div>
</div>
<div class="plan featured" style="left:436px;top:2003px;height:362px;width:328px">
  <div class="price" style="margin-top:64px">$1,495.00</div><div class="pline"></div>
  <h4>90 Day Post &amp;<br>Distributor Search Package</h4>
  <p class="desc">90-day post &amp; distributor search package Unlimited Featured Job Postings and access to our directory ...</p>
  <div class="btns"><span class="fill">MORE DETAIL</span><span>BUY NOW!</span></div>
</div>
<div class="plan" style="left:748px;top:2029px;height:310px">
  <div class="price">$3,495.00</div><div class="pline"></div>
  <h4>365 Day Post &amp;<br>Distributor Search Package</h4>
  <p class="desc">Eligible for "Easy Pay" billing over first (3) three months of product period*** Access our entire ...</p>
  <div class="btns"><span>MORE DETAIL</span><span>BUY NOW!</span></div>
</div>

<h2 class="section-title" style="left:0;width:1200px;text-align:center;top:2436px">Featured Lines</h2>

<table class="lines">
  <colgroup><col style="width:119px"><col style="width:111px"><col style="width:139px"><col style="width:161px"><col style="width:121px"><col style="width:119px"><col style="width:118px"></colgroup>
  <thead><tr><th>Title</th><th>Tracking ID</th><th>Location</th><th>Categories</th><th>Commission</th><th>Product Cost</th><th>Date Posted</th></tr></thead>
  <tbody>
    <tr><td>Another<br>Product</td><td>1043-18</td><td>Purchase a product<br>to view.</td><td>Capital Equipment<br>Diagnostic Imaging<br>Healthcare IT<br>Healthcare Software</td><td>11%-20%</td><td>$100-$500</td><td>12/6/2017</td></tr>
    <tr class="alt"><td>My Third<br>Product</td><td>1043-17</td><td>Purchase a product<br>to view.</td><td>Biotechnology/Tissue<br>Capital Equipment<br>Diagnostic Imaging<br>Disposables</td><td>5%-10%</td><td>$500-$500</td><td>12/1/2017</td></tr>
  </tbody>
</table>

<footer class="site-footer">
  <div class="fbrand"><i></i>RepHarborly</div>
  <p class="addr">4410 Harbor Ridge Blvd, Bayview, FL 33500</p>
  <p class="fcall">Call Us.: 555.214.0387</p>
  <div class="social"><span></span><span class="on"></span><span></span></div>
  <p class="copy">© 2018 RepHarborly.com<br>All Right Reserved.</p>
</footer>

</body>
</html>
```